New online premium luxury candle business needs a candle label design

We need a candle label design for a new premium candle company called Kind Mirabel. Kind Mirabel is a premium luxury candle brand with an ethical layer. For every candle sold, a girls school kit will be donated to girls in need in developing countries.
The name Kind Mirabel comes from the founders' grandmother, Mirabel, who enjoyed elegant classic vintage design and luxury old world travel to colourful tropical places and was a passionate believer in girls education.
We see the look and feel of Kind Mirabel being around warm whites, green palms and light woods, with a touch of vintage art deco font and design and with vintage botanical and tropical print background. The candle itself will be white, with a light wood lid.
LABEL LAYOUT
We see the label as warm white (either a square or a circle), and the content (words/art) as a light shiny gold colour. The square or circle will have a thin to medium borderline of gold, and it might be on its own or overlaid over a vintage tropical or botanical print square (*SEE EXAMPLES MARKED 1 ATTACHED*) for the label.
1. WORDS
Capitals KIND MIRABEL and (same font but smaller) underneath in middle CANDLES.
The font might either be vintage art deco (*SEE EXAMPLES MARKED 2 ATTACHED - note if a Condensed Vintage font -like font used (which might be my current favourite), the letters should be more closely brought together*) or a more elegant simple capitals eg in sans serif or as per the attached example (*SEE EXAMPLE MARKED 3 ATTACHED*.)
2. ART
The picture will be exactly the top half of the attached vintage trithrinax basilicus palm tree from end of the trunk upwards (*SEE EXAMPLE MARKED 4 ATTACHED*) (ie the full length green stems and leaves from the trunk rising out - so its as if the centre of the word lettering of KIND MIRABEL is the trunk and they will rise up out of the middle of the lettering. We could possibly lose that far left leaf dropping down if it looks too busy)
I'm not sure about the proportion of the leaves to the letters - one option could be for the leaves to be small over the middle of the lettering (*SEE EXAMPLE MARKED 6*), or another could be for them to be more proportionate with the lettering. What do you think?
There could be either a plain gold borderline around the white square/circle of the the label content, or it could have touches of art deco patterning around the edges of the words/art or the borderline or otherwise elegantly incorporated into the words/art? (*SEE EXAMPLES MARKED 5 ATTACHED*) - note I've attached some examples but don't feel restricted by these if you have an aligning vision of the pattern/something else that fits the brief! I don't want it to look 100% art deco themed, just elegant touches.
I might possibly want to create one version on white, and one version on black, (both with the colourful vintage tropical backgrounds behind the gold bordered black or white square or circle the words and art content are sitting in.) So the design in shiny light gold should be able to sit on both a black and a warm white background.
The final design should communicate premium 'high end' clean lined elegance, luxury and warmth, with vintage 1920s art deco and botanical/tropical old world luxury travel charm and a feel of palm beach and boho chic.
3. EXTRA NOTES ON CONTENT
Please note I'll need to leave room (about a quarter to a third on the bottom of the label) for word content to describe the candle characteristics and fragrance, for eg:
* Handpoured in Sydney * Soy wax *100% organic
* 300 grams *Essential oil infused
* Name of candle * Ingredients
Updates
Hi everyone, if you can please closely exactly follow each component of the brief specifications - all the designs so far have not followed them, and have incorporated too much art deco into the style. It was meant to be a touch around the border only and its meant to be kept simple. There will be two size candles, one medium and one large, the medium will be 6cm x 6cm, and the large 8cm x 8 cm. Thank you.
Target Market(s)
Luxury and ethically oriented consumers
Look and feel
Each slider illustrates characteristics of the customer's brand and the style your logo design should communicate.

```html
<!DOCTYPE html>
<html lang="en">
<head>
<meta charset="utf-8">
<title>Kind Mirabel Candles – Label</title>
<link rel="stylesheet" href="https://fonts.googleapis.com/css2?family=Josefin+Sans:wght@300;700&family=Oswald:wght@300&display=swap">
<style>
  :root {
    --backdrop: #f0ead6;
    --card: #f9f6ec;
    --label-cream: #f8f6ec;
    --gold: #cfae4a;
    --gold-text: #c1a25c;
    --teal-band: #a2cdbb;
    --leaf-dark: #3f8c55;
    --leaf-mid: #5da770;
    --leaf-light: #9ccdb0;
    --olive: #7e8c44;
    --olive-deep: #6b7c46;
  }
  * { margin: 0; padding: 0; box-sizing: border-box; }
  html, body {
    width: 1200px; height: 1200px; overflow: hidden;
    background: var(--backdrop);
  }
  .canvas { position: relative; width: 1200px; height: 1200px; }
  .label-card {
    position: absolute; left: 80px; top: 80px; width: 1040px; height: 1040px;
    background: var(--card);
    box-shadow: 0 2px 10px rgba(120, 100, 60, 0.12);
  }
  .tropical-print {
    position: absolute; left: 110px; top: 110px; width: 980px; height: 980px;
    background:
      radial-gradient(circle at 20% 25%, var(--leaf-dark) 0%, transparent 35%),
      radial-gradient(circle at 80% 75%, var(--leaf-dark) 0%, transparent 35%),
      radial-gradient(circle at 75% 15%, var(--leaf-light) 0%, transparent 30%),
      radial-gradient(circle at 15% 85%, var(--leaf-light) 0%, transparent 30%),
      linear-gradient(135deg, var(--leaf-mid), var(--leaf-light) 50%, var(--leaf-mid));
  }
  .frame { position: absolute; left: 0; top: 0; width: 1200px; height: 1200px; }
  .palm-art {
    position: absolute; left: 372px; top: 236px; width: 476px; height: 340px;
    background: radial-gradient(ellipse 55% 60% at 50% 40%, #5e8a36 0%, #7fa04c 45%, rgba(200, 215, 160, 0.35) 75%, rgba(248, 246, 236, 0) 100%);
  }
  .copy { position: absolute; left: 0; width: 1200px; text-align: center; white-space: nowrap; }
  .brand-name {
    top: 566px;
    font-family: "Josefin Sans", sans-serif; font-weight: 300;
    font-size: 88px; line-height: 96px; color: var(--olive);
    letter-spacing: 0.04em; padding-left: 0.04em;
  }
  .product-type {
    top: 686px;
    font-family: "Josefin Sans", sans-serif; font-weight: 700;
    font-size: 50px; line-height: 56px; color: var(--olive-deep);
    letter-spacing: 0.05em; padding-left: 0.05em;
  }
  .candle-weight {
    top: 800px;
    font-family: "Oswald", sans-serif; font-weight: 300;
    font-size: 38px; line-height: 44px; color: var(--gold-text);
  }
  .candle-name, .candle-details, .candle-ingredients {
    font-family: "Oswald", sans-serif; font-weight: 300; color: var(--gold-text);
  }
  .candle-name { top: 895px; font-size: 31px; line-height: 38px; }
  .candle-details { top: 936px; font-size: 23px; line-height: 30px; }
  .candle-ingredients { top: 968px; font-size: 23px; line-height: 30px; }
</style>
</head>
<body>
<main class="canvas">
  <div class="label-card"></div>
  <div class="tropical-print" role="img" aria-label="Watercolour tropical palm and monstera leaf print in greens"></div>

  <svg class="frame" viewBox="0 0 1200 1200" aria-hidden="true">
    <rect x="158" y="158" width="884" height="884" fill="var(--label-cream)" stroke="var(--gold)" stroke-width="5"/>
    <rect x="175" y="175" width="850" height="850" fill="none" stroke="var(--teal-band)" stroke-width="12"/>
    <rect x="193" y="193" width="814" height="814" fill="none" stroke="var(--gold)" stroke-width="4"/>
    <g fill="var(--label-cream)" stroke="var(--gold)" stroke-width="4">
      <rect x="171" y="170" width="80" height="82"/>
      <rect x="949" y="170" width="80" height="82"/>
      <rect x="171" y="948" width="80" height="82"/>
      <rect x="949" y="948" width="80" height="82"/>
    </g>
    <g fill="none" stroke="var(--gold)" stroke-width="4">
      <path d="M193 251 V193 H251"/>
      <path d="M949 193 H1007 V251"/>
      <path d="M193 949 V1007 H251"/>
      <path d="M1007 949 V1007 H949"/>
    </g>
  </svg>

  <div class="palm-art" role="img" aria-label="Vintage botanical illustration of a fan palm with green fronds rising from the title"></div>

  <h1 class="copy brand-name">KIND MIRABEL</h1>
  <p class="copy product-type">CANDLES</p>
  <p class="copy candle-weight">300 GRAMS</p>
  <p class="copy candle-name">NAME OF CANDLE</p>
  <p class="copy candle-details">HANDPOURED IN SYDNEY • SOY WAX • 100% ORGANIC • ESSENTIAL OIL INFUSED</p>
  <p class="copy candle-ingredients">INGREDIENTS : HERE YOU CAN WRITE A LISTS OF DIFFERENT INGREDIENTS</p>
</main>
</body>
</html>
```